Website Design for a "Talent Recruitment Agency"

We are looking for a website design for the website of our "Talent Recruitment Agency"; which is called "Crestway Hub".
Our recruitment website "Crestway Hub" will be focusing on: "Crestway Hub: Linking People & Firms in Switzerland"; which means our target audience is two-folded:
(i) TALENT - that is currently residing in- or outside of Switzerland, and is open for and interested in the "Swiss Job Market".
(ii) COMPANIES - that are looking for talent for specific job vacancies in Switzerland.
With our "Crestway Hub" approach we inted to focus on Membership & Partnership:
(a)"Membership"(TALENT)
and
(b)"Partnership"(COMPANIES)
Some of the competitor sites we like are:
• www.plimora42.dk
• www.qelvo.ch
• www.brandolix.ch/en
A sitemap example of our website is attached.
Also attached is a "Crestway Hub" logo in .eps format and one in .jpeg format.
We very much look forward to receive your creative ideas.
Best regards,
Crestway Hub
Crestway Hub: Linking People & Firms in Switzerland.
Website: crestwayhub.ch - Twitter: CrestwayHubCH
Target Market(s)
(i) TALENT (with around 0-10 years of working experience), currently residing in- or outside of Switzerland, but eligible to work in Switzerland.
(ii) COMPANIES (national or international) that are based in Switzerland.
Industry/Entity Type
Recruitment

```html
<!DOCTYPE html>
<html lang="en">
<head>
<meta charset="utf-8">
<title>Crestway Hub – Linking People &amp; Firms in Switzerland</title>
<link href="https://fonts.googleapis.com/css2?family=Yanone+Kaffeesatz:wght@300;400&family=Lato:wght@400;700&display=swap" rel="stylesheet">
<style>
:root{
  --orange:#f36f21;
  --orange-dark:#e85f14;
  --blue:#0a8fd0;
  --blue-deep:#0567b7;
  --blue-light:#1cc2ef;
  --ink:#222;
  --page:#f2f2f2;
  --white:#fff;
  --tab:#3a3a3a;
  --grey-mark:#c9c9c9;
}
*{box-sizing:border-box;margin:0;padding:0}
html,body{width:883px;height:1200px;overflow:hidden}
body{position:relative;background:var(--page);font-family:"Lato",Arial,sans-serif;color:var(--ink)}
.site-header{position:absolute;left:0;top:0;width:883px;height:106px;background:#efefef;display:flex;align-items:center;justify-content:center;gap:12px}
.brand-dot{width:44px;height:44px;border-radius:50%;background:var(--orange)}
.brand-name{font-family:"Lato",sans-serif;font-weight:700;font-size:34px;color:var(--blue)}
.main-nav{position:absolute;left:0;top:106px;width:883px;height:36px;background:linear-gradient(#ff8a44,var(--orange) 30%,var(--orange-dark));border-top:2px solid #ffb27f;display:flex;align-items:center}
.main-nav ul{list-style:none;display:flex;margin-left:88px;font-family:"Yanone Kaffeesatz",sans-serif;font-size:15px;color:#3a1500;letter-spacing:.3px}
.main-nav li{display:flex}
.main-nav li+li::before{content:"|";margin:0 26px}
.lang-select{position:absolute;left:693px;top:9px;width:98px;height:18px;background:var(--white);font-size:9px;color:#333;display:flex;align-items:center;padding-left:11px}
.lang-select svg{position:absolute;right:5px;top:5px}
.hero{position:absolute;left:0;top:144px;width:883px;height:300px;background:radial-gradient(ellipse at 50% 30%,var(--blue-light),var(--blue) 55%,var(--blue-deep))}
.intro{position:absolute;left:0;top:444px;width:883px;height:158px;background:linear-gradient(#fff,#f6f6f6);text-align:center}
.intro h1{margin-top:62px;font-family:"Yanone Kaffeesatz",sans-serif;font-weight:400;font-size:26px;color:var(--orange);text-transform:uppercase;letter-spacing:.3px}
.intro p{width:720px;margin:4px auto 0;font-size:13.4px;line-height:16px}
.audiences{position:absolute;left:0;top:602px;width:883px;height:356px;background:linear-gradient(#e8e8e8,#fdfdfd)}
.audience{position:absolute;top:0;width:297px}
.audience.talents{left:95px}
.audience.companies{left:469px}
.audience h2{margin-top:26px;text-align:center;font-family:"Yanone Kaffeesatz",sans-serif;font-weight:400;font-size:27px;color:var(--blue)}
.audience .rule{height:12px;margin:6px -18px 0;background:radial-gradient(ellipse at 50% 0,rgba(0,0,0,.55),rgba(0,0,0,0) 70%)}
.audience p{margin:18px 7px 0;font-size:10.6px;line-height:15px;text-align:justify}
.actions{position:absolute;top:240px;left:0;width:297px;display:flex;flex-direction:column;gap:4px}
.btn{height:29px;display:flex;align-items:center;justify-content:center;color:var(--white);font-size:13.5px;text-transform:uppercase;background:var(--orange)}
.btn.alt{background:var(--blue)}
.partners{position:absolute;left:0;top:958px;width:883px;height:187px;background:linear-gradient(#e9e9e9,#f3f3f3)}
.partners-tab{position:absolute;left:365px;top:41px;width:120px;height:27px;border-radius:9px 9px 0 0;background:var(--tab);color:var(--white);font-family:"Yanone Kaffeesatz",sans-serif;font-size:18px;text-align:center;line-height:28px;letter-spacing:.4px}
.partners-strip{position:absolute;left:95px;top:67px;width:671px;height:87px;border-radius:22px;background:var(--white);box-shadow:0 2px 6px rgba(0,0,0,.25);display:flex;align-items:center;justify-content:space-around;padding:0 50px}
.partner-badge{width:74px;height:22px;border-radius:4px;background:var(--grey-mark)}
.partner-badge.round{width:72px;height:40px;border-radius:50%}
.carousel-arrow{position:absolute;top:26px}
.carousel-arrow.prev{left:-3px}
.carousel-arrow.next{right:-3px}
.site-footer{position:absolute;left:0;top:1145px;width:883px;height:55px;background:var(--blue);color:var(--white);font-size:9.5px}
.footer-links{position:absolute;left:95px;top:19px;list-style:none;display:flex}
.footer-links li+li::before{content:"|";margin:0 5px}
.copyright{position:absolute;left:95px;top:33px}
.social{position:absolute;left:627px;top:19px;display:flex;gap:12px}
.social span{width:23px;height:23px;border-radius:50%;background:var(--white)}
</style>
</head>
<body>
<header class="site-header">
  <span class="brand-dot"></span>
  <span class="brand-name">Crestway Hub</span>
</header>

<nav class="main-nav">
  <ul>
    <li>HOME</li><li>ABOUT</li><li>TALENT</li><li>COMPANIES</li><li>JOBS</li><li>EVENTS</li><li>CONTACT</li>
  </ul>
  <div class="lang-select">Select Language
    <svg width="10" height="8" viewBox="0 0 10 8"><path d="M1 1l4 4 4-4" fill="none" stroke="#222" stroke-width="2"/></svg>
  </div>
</nav>

<div class="hero" role="img" aria-label="Silhouettes of five business people standing in front of a glowing blue world map"></div>

<section class="intro">
  <h1>Crestway Hub: Linking People &amp; Firms in Switzerland</h1>
  <p>Lorem ipsum dolor sit amet, consectetur adipiscing elit. Quisque at vulputate sem. Sed cursus at nibh ac hendrerit. Proin lectus dui, blandit ac ultricies a, ultrices at lacus.</p>
</section>

<section class="audiences">
  <div class="audience talents">
    <h2>TALENTS</h2>
    <div class="rule"></div>
    <p>Maecenas urna eros, semper et metus sed, iaculis porttitor lacus. Aenean in velit sit amet odio lacinia tempor et eu neque. Etiam id ipsum ut urna ultricies porta. Ut congue scelerisque ligula, ut auctor velit. Vestibulum ante ipsum primis in faucibus orci luctus et ultrices posuere cubilia Curae; Aenean aliquam, erat at congue condimentum, enim est convallis nulla, quis sollicitudin libero dolor a felis. Integer sit amet cursus nulla. Sed pharetra commodo viverra.</p>
    <div class="actions">
      <a class="btn">Membership &amp; Benefits</a>
      <a class="btn alt">Get Registered</a>
      <a class="btn">CV Uploads</a>
    </div>
  </div>
  <div class="audience companies">
    <h2>COMPANIES</h2>
    <div class="rule"></div>
    <p>Maecenas urna eros, semper et metus sed, iaculis porttitor lacus. Aenean in velit sit amet odio lacinia tempor et eu neque. Etiam id ipsum ut urna ultricies porta. Ut congue scelerisque ligula, ut auctor velit. Vestibulum ante ipsum primis in faucibus orci luctus et ultrices posuere cubilia Curae; Aenean aliquam, erat at congue condimentum, enim est convallis nulla, quis sollicitudin libero dolor a felis. Integer sit amet cursus nulla. Sed pharetra commodo viverra.</p>
    <div class="actions">
      <a class="btn">Login&nbsp; | &nbsp;Registration</a>
      <a class="btn alt">Partnerships &amp; Benefits</a>
      <a class="btn">Talent Request</a>
    </div>
  </div>
</section>

<section class="partners">
  <div class="partners-tab">OUR PARTNERS</div>
  <div class="partners-strip">
    <svg class="carousel-arrow prev" width="14" height="34" viewBox="0 0 14 34"><path d="M14 0a17 17 0 0 0 0 34z" fill="#666"/><path d="M9 13l-4 4 4 4z" fill="#fff"/></svg>
    <span class="partner-badge"></span>
    <span class="partner-badge"></span>
    <span class="partner-badge round"></span>
    <span class="partner-badge"></span>
    <span class="partner-badge"></span>
    <svg class="carousel-arrow next" width="14" height="34" viewBox="0 0 14 34"><path d="M0 0a17 17 0 0 1 0 34z" fill="#666"/><path d="M5 13l4 4-4 4z" fill="#fff"/></svg>
  </div>
</section>

<footer class="site-footer">
  <ul class="footer-links">
    <li>Home</li><li>About</li><li>Talent</li><li>Companies</li><li>Jobs</li><li>Events</li><li>Contact</li>
  </ul>
  <div class="copyright">© 2014, All Rights Reseved</div>
  <div class="social"><span></span><span></span><span></span><span></span></div>
</footer>
</body>
</html>
```